Signage Design job – Healthcare IT Company Needs a Core Values Poster for Office

We want to make a poster for our offices that beautifully presents our core values.

We want the design to be fun, young and colourful while showing some sophistication.

The poster will be visible to the staff (within the open plan office), and the right colours will need to be used to enhance mood and productivity. Perhaps we could be looking at a colour for each core value? Or potentially some other way for each value to stand out? We have other culture posters that have been created in the past that we would like to stay similar to in style for cohesiveness.

Our office walls are primarily white and navy blue with accents of orange, grey, and turquoise.

In terms of size - we aren't 100% on what size we want, but not only will be print it on the walls, we will also be printing out mini versions for people to put in their cubicles so keep that in mind for font legibility.

Fonts can be experimented with, but they main body font should be Source Sans Pro.

It needs to be clear, punchy and stand out from across the office (while being easy on the eye)

We have a series of cartoon guardians that can be incorporated into the design as well.

I have attached a few sample images that can be used as inspiration. We would like more colour throughout the design. 

Final file should be AI or EPS vector file.

Target Market(s)

Internal employees age range from 25-60

Font styles to use
Sans Serif
Other font styles liked:
• Please use Source Sans Pro

Colors
abd037
6b449b
33a6d7
f37122
0355a3
ffcf3e
e34297

Requirements
Must have
• Must use our colors. Must feel fresh and energetic. Must emphasize important key words. Must feel inspirational. Must align with our internal branding. Look at the 4 posters I have included in the files to understand our look. Our company website is www.velmarohealth.com
Nice to have
• Mission Statement is not necessary if there isn't enough room on the poster.
Should not have
• Should not be cluttered looking in such a way that you can't get the message.

```html
<!DOCTYPE html>
<html lang="en">
<head>
<meta charset="utf-8">
<title>Velmaro Health – Core Values</title>
<link href="https://fonts.googleapis.com/css2?family=Roboto:wght@400;500;700;900&family=Montserrat:wght@800&display=swap" rel="stylesheet">
<style>
  :root {
    --navy: #0b2c5e;
    --orange: #f2501c;
    --ink: #141414;
    --page: #ffffff;
    --lime: #abd037;
    --violet: #6b449b;
    --sky: #33a6d7;
    --tangerine: #f37122;
  }
  * { box-sizing: border-box; margin: 0; padding: 0; }
  html, body { width: 979px; height: 1200px; overflow: hidden; background: var(--page); }
  body { font-family: "Roboto", sans-serif; color: var(--ink); position: relative; }

  .poster { position: absolute; left: 0; top: 0; width: 979px; height: 1200px; background: var(--page); overflow: hidden; }

  .brand { position: absolute; left: 46px; top: 36px; display: flex; align-items: center; gap: 22px; }
  .brand-dot { width: 78px; height: 78px; border-radius: 50%; background: var(--orange); }
  .brand-name { font-weight: 900; font-size: 62px; letter-spacing: -1.5px; color: var(--navy); }

  .rule { position: absolute; left: 0; width: 979px; background: var(--orange); }
  .rule-top { top: 141px; height: 3px; }
  .rule-bottom { top: 1110px; height: 4px; }

  .hero-photo { position: absolute; left: 0; top: 144px; width: 979px; height: 470px;
    background: linear-gradient(90deg, #ffffff 0%, #f7f8f9 35%, #e9eef1 55%, #dde4e8 75%, #d6dde1 100%); }
  .hero-curve { position: absolute; left: 0; top: 530px; width: 979px; height: 84px; }

  .value-list { position: absolute; left: 0; top: 0; list-style: none; }
  .value-item { position: absolute; display: flex; align-items: center; gap: 19px; font-size: 22.5px; color: var(--ink); white-space: nowrap; }
  .value-icon { width: 36px; height: 36px; flex: none; }

  .headline { position: absolute; left: 36px; top: 615px; font-family: "Montserrat", sans-serif; font-weight: 800; font-size: 44px; letter-spacing: 1px; line-height: 1; }
  .section-title { position: absolute; font-weight: 400; font-size: 38px; line-height: 1; color: var(--ink); }
  .body-copy { position: absolute; font-size: 17px; line-height: 21.6px; text-align: justify; }

  .spirit-title { left: 36px; top: 674px; }
  .spirit-copy { left: 36px; top: 728px; width: 403px; }
  .values-title { left: 489px; top: 614px; }
  .values-copy { left: 489px; top: 661px; width: 450px; }
  .commitment-title { left: 489px; top: 763px; }
  .commitment-copy { left: 489px; top: 808px; width: 450px; }
  .team-title { left: 38px; top: 933px; }
  .team-copy { left: 38px; top: 981px; width: 890px; font-size: 16.5px; line-height: 21px; }

  .pillars { position: absolute; left: 0; top: 1122px; width: 979px; height: 44px; }
  .pillar { position: absolute; top: 0; height: 44px; display: flex; align-items: center; gap: 10px; }
  .pillar-badge { width: 44px; height: 44px; border-radius: 50%; flex: none; }
  .badge-lime { background: var(--lime); }
  .badge-violet { background: var(--violet); }
  .badge-sky { background: var(--sky); }
  .badge-tangerine { background: var(--tangerine); }
  .pillar-label { font-size: 11px; line-height: 13px; color: #333; }
</style>
</head>
<body>
<main class="poster">
  <header class="brand">
    <span class="brand-dot"></span>
    <span class="brand-name">Velmaro Health</span>
  </header>
  <div class="rule rule-top"></div>

  <div class="hero-photo" role="img" aria-label="Photo of two doctors in white coats with stethoscopes looking at a laptop in a bright clinic"></div>
  <svg class="hero-curve" viewBox="0 0 979 84" preserveAspectRatio="none" aria-hidden="true">
    <path d="M0 26 Q490 120 979 31 L979 84 L0 84 Z" fill="#ffffff"/>
    <path d="M0 26 Q490 120 979 31" fill="none" stroke="#f2501c" stroke-width="3"/>
  </svg>

  <ul class="value-list">
    <li class="value-item" style="left:37px;top:158px"><svg class="value-icon" viewBox="0 0 36 36"><circle cx="18" cy="18" r="16.5" fill="#fff" stroke="#f2501c" stroke-width="2"/><path d="M10 25h16M12 24v-4M16 24v-6M20 24v-8M24 24v-10" stroke="#222" stroke-width="1.6" fill="none"/></svg>Pioneer</li>
    <li class="value-item" style="left:37px;top:207px"><svg class="value-icon" viewBox="0 0 36 36"><circle cx="18" cy="18" r="16.5" fill="#fff" stroke="#f2501c" stroke-width="2"/><path d="M9 16l5-3 4 3 4-3 5 3-5 6h-8z" stroke="#222" stroke-width="1.5" fill="none"/></svg>Collaborative</li>
    <li class="value-item" style="left:37px;top:257px"><svg class="value-icon" viewBox="0 0 36 36"><circle cx="18" cy="18" r="16.5" fill="#fff" stroke="#f2501c" stroke-width="2"/><circle cx="18" cy="17" r="7" stroke="#222" stroke-width="1.5" fill="none"/><path d="M15 24v3h6" stroke="#222" stroke-width="1.5" fill="none"/></svg>Passionate</li>
    <li class="value-item" style="left:37px;top:304px"><svg class="value-icon" viewBox="0 0 36 36"><circle cx="18" cy="18" r="16.5" fill="#fff" stroke="#f2501c" stroke-width="2"/><circle cx="15" cy="18" r="5.5" stroke="#222" stroke-width="1.5" fill="none"/><circle cx="21" cy="18" r="5.5" stroke="#222" stroke-width="1.5" fill="none"/></svg>Integrity</li>
    <li class="value-item" style="left:37px;top:353px"><svg class="value-icon" viewBox="0 0 36 36"><circle cx="18" cy="18" r="16.5" fill="#fff" stroke="#f2501c" stroke-width="2"/><rect x="10" y="12" width="16" height="10" stroke="#222" stroke-width="1.5" fill="none"/><path d="M14 26h8M18 22v4" stroke="#222" stroke-width="1.5"/></svg>Adaptable</li>
    <li class="value-item" style="left:37px;top:403px"><svg class="value-icon" viewBox="0 0 36 36"><circle cx="18" cy="18" r="16.5" fill="#fff" stroke="#f2501c" stroke-width="2"/><path d="M11 17h4v9h-4zM15 17l4-7c2 0 2 2 1 5h5l-1 11h-9" stroke="#222" stroke-width="1.5" fill="none"/></svg>Excellence</li>
    <li class="value-item" style="left:37px;top:452px"><svg class="value-icon" viewBox="0 0 36 36"><circle cx="18" cy="18" r="16.5" fill="#fff" stroke="#f2501c" stroke-width="2"/><path d="M11 16a7 7 0 0 1 13-2M25 20a7 7 0 0 1-13 2" stroke="#222" stroke-width="1.5" fill="none"/><path d="M24 10v4h-4M12 26v-4h4" stroke="#222" stroke-width="1.5" fill="none"/></svg>Agile</li>
    <li class="value-item" style="left:37px;top:503px"><svg class="value-icon" viewBox="0 0 36 36"><circle cx="18" cy="18" r="16.5" fill="#fff" stroke="#f2501c" stroke-width="2"/><circle cx="13" cy="14" r="3" stroke="#222" stroke-width="1.5" fill="none"/><circle cx="23" cy="14" r="3" stroke="#222" stroke-width="1.5" fill="none"/><path d="M8 25c1-5 9-5 10 0M18 25c1-5 9-5 10 0" stroke="#222" stroke-width="1.5" fill="none"/></svg>Resourceful</li>

    <li class="value-item" style="left:278px;top:158px"><svg class="value-icon" viewBox="0 0 36 36"><circle cx="18" cy="18" r="16.5" fill="#fff" stroke="#f2501c" stroke-width="2"/><circle cx="18" cy="14" r="4" stroke="#222" stroke-width="1.5" fill="none"/><path d="M10 26c1-6 15-6 16 0z" stroke="#222" stroke-width="1.5" fill="none"/></svg>Entrepreneurial</li>
    <li class="value-item" style="left:278px;top:208px"><svg class="value-icon" viewBox="0 0 36 36"><circle cx="18" cy="18" r="16.5" fill="#fff" stroke="#f2501c" stroke-width="2"/><circle cx="17" cy="10" r="2" fill="#222"/><path d="M17 13l-2 6 2 8M17 13l3 5" stroke="#222" stroke-width="1.8" fill="none"/></svg>Respectful</li>
    <li class="value-item" style="left:278px;top:255px"><svg class="value-icon" viewBox="0 0 36 36"><circle cx="18" cy="18" r="16.5" fill="#fff" stroke="#f2501c" stroke-width="2"/><path d="M11 11h6v5h-6zM19 20h6v5h-6zM14 16v7h5" stroke="#222" stroke-width="1.5" fill="none"/></svg>Solutions</li>
    <li class="value-item" style="left:278px;top:305px"><svg class="value-icon" viewBox="0 0 36 36"><circle cx="18" cy="18" r="16.5" fill="#fff" stroke="#f2501c" stroke-width="2"/><rect x="13" y="9" width="10" height="18" rx="1" stroke="#222" stroke-width="1.5" fill="none"/><path d="M15 13h6M15 17h6M15 21h6" stroke="#222" stroke-width="1.3"/></svg>Accountable</li>
    <li class="value-item" style="left:278px;top:353px"><svg class="value-icon" viewBox="0 0 36 36"><circle cx="18" cy="18" r="16.5" fill="#fff" stroke="#f2501c" stroke-width="2"/><path d="M13 10c-3 6 0 12 5 12s8-6 5-12M18 22v5" stroke="#222" stroke-width="1.5" fill="none"/></svg>Driven</li>
    <li class="value-item" style="left:278px;top:404px"><svg class="value-icon" viewBox="0 0 36 36"><circle cx="18" cy="18" r="16.5" fill="#fff" stroke="#f2501c" stroke-width="2"/><circle cx="18" cy="13" r="4" stroke="#222" stroke-width="1.5" fill="none"/><path d="M11 27v-3c0-4 14-4 14 0v3z" stroke="#222" stroke-width="1.5" fill="none"/></svg>Selfless</li>
    <li class="value-item" style="left:278px;top:452px"><svg class="value-icon" viewBox="0 0 36 36"><circle cx="18" cy="18" r="16.5" fill="#fff" stroke="#f2501c" stroke-width="2"/><rect x="11" y="10" width="14" height="16" stroke="#222" stroke-width="1.5" fill="none"/><path d="M14 14h8M14 18h8M14 22h5" stroke="#222" stroke-width="1.3"/></svg>Disciplined</li>
    <li class="value-item" style="left:278px;top:504px"><svg class="value-icon" viewBox="0 0 36 36"><circle cx="18" cy="18" r="16.5" fill="#fff" stroke="#f2501c" stroke-width="2"/><path d="M9 23h6l5 2 7-4M18 19v-7M18 12c3 0 5 2 5 4M18 14c-2 0-4 1-4 3" stroke="#222" stroke-width="1.5" fill="none"/></svg>Growth</li>
  </ul>

  <h1 class="headline">WHO WE ARE</h1>

  <h2 class="section-title spirit-title">Our Spirit</h2>
  <p class="body-copy spirit-copy">Velmaro Health was founded to benefit doctors and healthcare providers. We PIONEER technologies and services that are simple, powerful, and fast, which help doctors provide excellent patient care on their own terms. We have an ENTREPRENEURIAL spirit. We are ADAPTABLE, DRIVEN, and innovative. Our focus is broad, reaching horizontally through the healthcare space.</p>

  <h2 class="section-title values-title">Our Values</h2>
  <p class="body-copy values-copy">We are COLLABORATIVE and communicate openly, honestly, and RESPECTFULLY at all levels. We challenge ourselves to EXCELLENCE, we are SELFLESS, generous, and contribute at our highest capacity.</p>

  <h2 class="section-title commitment-title">Our Commitment</h2>
  <p class="body-copy commitment-copy">We conduct business with INTEGRITY. We are ACCOUNTABLE to one another, our customers, and our partners. We strive to maintain affordable prices by being good stewards of our RESOURCES. We are committed to having a GROWTH mindset and doing our best today and doing better tomorrow.</p>

  <h2 class="section-title team-title">Our Values</h2>
  <p class="body-copy team-copy">We are members of a team, and we recognize that our combined efforts make us successful. We welcome challenges and embrace change. We are PASSIONATE about our vision, actively expressing our ideas, and making room for constructive dissent. We are SOLUTIONS oriented, take risks, think differently, and pave our own way as a leader in the market. We are AGILE and “fail fast”. We are DISCIPLINED to think carefully, plan well, measure our results, and manage the outcomes so that we can succeed in a competitive environment.</p>

  <div class="rule rule-bottom"></div>

  <div class="pillars">
    <div class="pillar" style="left:46px"><span class="pillar-badge badge-lime"></span><span class="pillar-label">Personal and<br>Professional Growth</span></div>
    <div class="pillar" style="left:302px"><span class="pillar-badge badge-violet"></span><span class="pillar-label">Be Your Best Self</span></div>
    <div class="pillar" style="left:538px"><span class="pillar-badge badge-sky"></span><span class="pillar-label">Innovation and<br>Strategy</span></div>
    <div class="pillar" style="left:790px"><span class="pillar-badge badge-tangerine"></span><span class="pillar-label">Cultivating<br>Collaboration</span></div>
  </div>
</main>
</body>
</html>
```